Fernhollow Glow Clinic is a rebranding of fernhollowfootcare.com.au. The business provides Medical Injectables (botox and fillers) Laser and IPL therapies, Podiatry and remedial massage. We have a logo already done (yay! sketch hive!) you can download it here: http://fernhollowglowclinic.com/brand_assets.zip . We are after a clean, long scrolling website (in the style of quvaret.com). There will be 6 subpages (or sections depending on how you create it) (1) Cosmetic Injections (2) Podiatry (3) Remedial Massage (4) Laser Therapies (5) Skin Care (6) Customer Club and Special Offers. The target demographic is wealthy or aspirational women 35+.

Font styles to use
Sans Serif

Colors
9bcb3c
33a6d7

Requirements
Must have
• Simple, clean long scroller like quvaret.com
Nice to have
• Congruence with existing corporate identity.

```html
<!DOCTYPE html>
<html lang="en">
<head>
<meta charset="utf-8">
<title>Fernhollow Glow Clinic</title>
<link rel="stylesheet" href="https://fonts.googleapis.com/css2?family=Arimo:wght@400;700&family=Playball&display=swap">
<style>
:root{
  --blue:#33a6d7;
  --blue-deep:#1479bd;
  --hex-blue:#1e8fd0;
  --green:#9bcb3c;
  --navy:#1f2d5c;
  --about:#2e3f74;
  --sage:#c8d3b6;
  --voucher-bg:#f3ece8;
  --purple:#8d72b4;
  --contact:#b1554b;
  --footer:#2b2020;
  --ink:#333;
  --white:#fff;
}
*{box-sizing:border-box;margin:0;padding:0}
html,body{width:1200px;height:4663px;overflow:hidden}
body{position:relative;font-family:"Arimo",Arial,sans-serif;color:var(--ink);background:var(--white)}
section,header,footer{position:absolute;left:0;width:1200px;overflow:hidden}
.photo{position:absolute}
.section-title{position:absolute;left:0;width:1200px;text-align:center;font-weight:400;font-size:32px}

/* Header & hero */
.hero{top:0;height:709px;background:linear-gradient(180deg,#eaf8fd 0%,#c8ecf8 60%,#a9e0f4 100%)}
.brand{position:absolute;top:40px;left:0;width:1200px;text-align:center;font-size:26px;font-weight:700;color:var(--blue-deep);letter-spacing:1px}
.brand-dot{display:inline-block;width:14px;height:14px;border-radius:50%;background:var(--green);margin-right:10px;vertical-align:middle}
.nav{position:absolute;top:112px;left:0;width:1200px;display:flex;justify-content:center;gap:30px;font-size:17px}
.nav a{color:#2d3a4a;text-decoration:none}
.nav a.current{color:var(--blue)}
.nav-mark{position:absolute;top:86px;left:222px}
.hero-photo{left:0;top:150px;width:620px;height:559px;background:radial-gradient(ellipse at 40% 45%,#f1d3bd 0%,#d8b8a0 35%,#bfe5f3 75%,rgba(191,229,243,0) 100%)}
.hero-quote{position:absolute;left:590px;top:245px;width:620px;text-align:center;font-family:"Playball",cursive;font-size:33px;line-height:40px;color:var(--navy)}

/* About */
.about{top:709px;height:581px;background:var(--about)}
.about-photo{inset:0;background:linear-gradient(120deg,#35467c 0%,#4d5a8c 45%,#2d3c6e 100%);opacity:.9}
.about .section-title{top:148px;color:var(--white)}
.about-text{position:absolute;left:218px;top:240px;width:777px;text-align:center;color:var(--white);font-size:14px;line-height:18px}

/* Services */
.services{top:1290px;height:566px;background:var(--sage)}
.services-photo{inset:0;background:linear-gradient(100deg,#d6dec8 0%,#c3cfae 55%,#b3c09e 100%)}
.services .section-title{top:60px;color:var(--blue)}
.service-list{position:absolute;top:228px;left:0;width:1200px;list-style:none}
.service{position:absolute;width:150px;text-align:center}
.service svg{display:block;margin:0 auto}
.service span{display:block;margin-top:10px;color:var(--blue-deep);font-weight:700;font-size:14px;line-height:16px}

/* Specials */
.specials{top:1856px;height:538px;background:var(--blue-deep)}
.specials .section-title{top:44px;color:var(--white)}
.specials-photo{right:40px;top:70px;width:230px;height:380px;background:radial-gradient(ellipse at 50% 60%,rgba(20,60,110,.55) 0%,rgba(20,121,189,0) 70%)}
.package{position:absolute;left:177px;width:900px;color:var(--white);font-size:14px;line-height:18px}
.package h3{font-size:17px;font-weight:700;margin-bottom:6px}

/* Gift vouchers */
.vouchers{top:2394px;height:731px;background:var(--voucher-bg)}
.vouchers-photo{inset:0;background:linear-gradient(160deg,#f6efec 0%,#ead9d1 50%,#f4ece8 100%)}
.vouchers .section-title{top:44px;color:var(--blue)}
.vouchers-body{position:absolute;left:177px;top:120px;width:850px;font-size:14px;line-height:18px;color:#333}
.vouchers-body h3{color:var(--blue-deep);font-size:17px;font-weight:700;margin-bottom:6px}
.vouchers-body p{margin-bottom:14px}
.voucher-card{position:absolute;left:177px;top:404px;width:843px;height:305px;background:var(--white);box-shadow:0 2px 8px rgba(0,0,0,.2)}
.voucher-text{position:absolute;left:150px;top:26px;width:400px;text-align:center;font-size:14px;line-height:19px;color:#333}
.voucher-brand{font-size:20px;font-weight:700;color:var(--blue-deep);margin-bottom:20px}
.voucher-amount{font-size:20px;font-weight:700}
.gift-photo{left:585px;top:36px;width:190px;height:230px;background:linear-gradient(160deg,#f7f2f4 0%,#e9d6de 60%,#c53c7a 100%);border-radius:6px}

/* Product range */
.products{top:3125px;height:559px;background:var(--purple)}
.products-photo{inset:0;background:linear-gradient(110deg,#9a82be 0%,#876db0 50%,#a08bc4 100%)}
.products .section-title{top:104px;color:var(--white)}
.products-text{position:absolute;left:300px;top:206px;width:600px;text-align:center;color:var(--white);font-size:14px;line-height:18px}
.products-text p{margin-bottom:14px}

/* Contact */
.contact{top:3684px;height:550px;background:var(--contact)}
.contact-photo{left:0;top:0;width:520px;height:550px;background:linear-gradient(90deg,#d9a290 0%,#c07363 60%,rgba(177,85,75,0) 100%)}
.contact .section-title{top:44px;color:var(--white)}
.contact-form{position:absolute;left:463px;top:134px;width:330px}
.field{display:block;width:330px;height:46px;border:none;background:var(--white);padding:0 12px;font-family:inherit;font-size:14px;color:#999;margin-bottom:13px;line-height:46px}
.field.message{height:115px;line-height:normal;padding-top:12px}
.send{display:block;width:78px;height:30px;background:var(--blue);color:var(--white);font-size:14px;line-height:30px;text-align:center;margin-top:12px}
.contact-info{position:absolute;left:802px;top:134px;width:255px;text-align:center;color:var(--white);font-size:14px;line-height:18px}
.contact-info h4{font-size:17px;font-weight:700;margin-top:6px}
.contact-info p{margin-bottom:10px}

/* Map & footer */
.map{top:4234px;height:367px;background:linear-gradient(180deg,#dfe6d6 0%,#e9ecdf 50%,#d6e2d2 100%)}
.footer{top:4601px;height:62px;background:var(--footer);text-align:center;color:#cfc6c6;font-size:11px}
.social{display:flex;justify-content:center;gap:8px;margin-top:12px}
.social span{width:22px;height:22px;border-radius:50%;border:2px solid #cfc6c6}
.copyright{margin-top:6px}
</style>
</head>
<body>

<header class="hero">
  <div class="photo hero-photo" role="img" aria-label="Woman relaxing on a spa towel"></div>
  <div class="brand"><span class="brand-dot"></span>Fernhollow Glow Clinic</div>
  <svg class="nav-mark" width="24" height="10" viewBox="0 0 24 10"><path d="M2 2 Q12 12 22 2" fill="none" stroke="var(--blue)" stroke-width="3"/></svg>
  <nav class="nav">
    <a class="current" href="#home">Home</a>
    <a href="#about">About Us</a>
    <a href="#services">Services</a>
    <a href="#specials">Specials/Packages</a>
    <a href="#vouchers">Gift Vouchers</a>
    <a href="#products">Product Range</a>
    <a href="#contact">Contact</a>
  </nav>
  <p class="hero-quote">Willowmere Spa offers the ultimate in<br>holistic skin and body treatments<br>especially designed to release ten-<br>sion, pamper and nurture the<br>whole body, bring tranquility,<br>balance and harmony in our busy<br>lives.</p>
</header>

<section class="about" id="about">
  <div class="photo about-photo" role="img" aria-label="Facial treatment in progress"></div>
  <h2 class="section-title">About Us</h2>
  <p class="about-text">Dummy text is also used to demonstrate the appearance of different typefaces and layouts, and in general the content of dummy text is nonsensical. Due to its widespread use as filler text for layouts, non-readability is of great importance: human perception is tuned to recognize certain patterns and repetitions in texts. If the distribution of letters and 'words' is random, the reader will not be distracted from making a neutral judgement on the visual impact and readability of the typefaces (typography), or the distribution of text on the page (layout or type area). For this reason, dummy text usually consists of a more or less random series of words or syllables. This prevents repetitive patterns from impairing the overall visual impression and facilitates the comparison of different typefaces. Furthermore, it is advantageous when the dummy text is relatively realistic so that the layout impression of the final publication is not compromised.</p>
</section>

<section class="services" id="services">
  <div class="photo services-photo" role="img" aria-label="Woman receiving a relaxing massage"></div>
  <h2 class="section-title">Services</h2>
  <ul class="service-list">
    <li class="service" style="left:158px"><svg width="124" height="138" viewBox="0 0 124 138"><polygon points="62,2 122,36 122,102 62,136 2,102 2,36" fill="var(--hex-blue)"/><circle cx="62" cy="69" r="24" fill="none" stroke="#fff" stroke-width="3"/></svg><span>Cosmetic<br>Injections</span></li>
    <li class="service" style="left:304px"><svg width="124" height="138" viewBox="0 0 124 138"><polygon points="62,2 122,36 122,102 62,136 2,102 2,36" fill="var(--hex-blue)"/><circle cx="62" cy="69" r="24" fill="none" stroke="#fff" stroke-width="3"/></svg><span>Podiatry</span></li>
    <li class="service" style="left:450px"><svg width="124" height="138" viewBox="0 0 124 138"><polygon points="62,2 122,36 122,102 62,136 2,102 2,36" fill="var(--hex-blue)"/><circle cx="62" cy="69" r="24" fill="none" stroke="#fff" stroke-width="3"/></svg><span>Remedial Massage</span></li>
    <li class="service" style="left:593px"><svg width="124" height="138" viewBox="0 0 124 138"><polygon points="62,2 122,36 122,102 62,136 2,102 2,36" fill="var(--hex-blue)"/><circle cx="62" cy="69" r="24" fill="none" stroke="#fff" stroke-width="3"/></svg><span>Laser Therapies</span></li>
    <li class="service" style="left:740px"><svg width="124" height="138" viewBox="0 0 124 138"><polygon points="62,2 122,36 122,102 62,136 2,102 2,36" fill="var(--hex-blue)"/><circle cx="62" cy="69" r="24" fill="none" stroke="#fff" stroke-width="3"/></svg><span>Skin Care</span></li>
    <li class="service" style="left:886px"><svg width="124" height="138" viewBox="0 0 124 138"><polygon points="62,2 122,36 122,102 62,136 2,102 2,36" fill="var(--hex-blue)"/><circle cx="62" cy="69" r="24" fill="none" stroke="#fff" stroke-width="3"/></svg><span>Customer Club<br>and Special Offers</span></li>
  </ul>
</section>

<section class="specials" id="specials">
  <div class="photo specials-photo" role="img" aria-label="Butterfly resting on stacked stones"></div>
  <h2 class="section-title">Specials/Packages</h2>
  <article class="package" style="top:138px">
    <h3>Spring Awakening</h3>
    <p>Give your body a new lease of life with this spa package offer. Includes a steam chamber session followed by a customised<br>facial, scalp massage, and hand and arm massage.<br>Was €95 NOW ONLY €69</p>
  </article>
  <article class="package" style="top:240px">
    <h3>Spring Refresher</h3>
    <p>Relax, unwind and breathe in the scent of Spring with a fabulous aromatherapy bath followed by either a customised facial<br>or full body massage.<br>Was €125 NOW ONLY €89</p>
  </article>
  <article class="package" style="top:342px">
    <h3>Spring Refresher</h3>
    <p>Banish those unwanted extra inches that may have snuck up on you over winter with a universal contour wrap. Then<br>choose from either a file and polish on your hands, a refresher facial, or a 30 minute reflexology treatment.<br>Was €130 NOW ONLY €90</p>
  </article>
</section>

<section class="vouchers" id="vouchers">
  <div class="photo vouchers-photo" role="img" aria-label="Hands holding a flower over water"></div>
  <h2 class="section-title">Gift Vouchers</h2>
  <div class="vouchers-body">
    <h3>Fernhollow Treatment Gift Vouchers</h3>
    <p>Dummy text is text that is used in the publishing industry or by web designers to occupy the space which will later be filled with 'real' content. This is required when, for example, the final text is not yet available. Dummy text is also known as 'fill text'. It is said that song composers of the past used dummy texts as lyrics when writing melodies in order to have a 'ready-made' text to sing with the melody. Dummy texts have been in use by typesetters since the 16th century.</p>
    <h3>SPA GIFT PACKAGES</h3>
    <p>Pamper Package for Her: Deep Cleansing Facial or Veridian Manual Facial, Fernhollow Ultimate Relaxation Massage, File and Polish, 2hrs 20 mins £150.</p>
    <p>Pure Indulgence Package: Foot Ritual, Customised Organic Facial, Red Rate Body Scrub, Hot Poultice and Warm Coconut Oil Body Massage, 2hrs 20 mins £170.</p>
  </div>
  <div class="voucher-card">
    <div class="voucher-text">
      <p class="voucher-brand">Fernhollow Glow Clinic</p>
      <p>Gift Voucher<br>To Ava Linton<br>From Fernhollow Glow Clinic</p>
      <p class="voucher-amount">$200</p>
      <p>e-Verification code FGC1000</p>
      <p style="margin-top:14px">Fernhollow<br>27 Larch Road,<br>Brightmoor</p>
    </div>
    <div class="photo gift-photo" role="img" aria-label="White gift box tied with a pink ribbon"></div>
  </div>
</section>

<section class="products" id="products">
  <div class="photo products-photo" role="img" aria-label="Feet during a pedicure treatment"></div>
  <h2 class="section-title">Product Range</h2>
  <div class="products-text">
    <p>We utilise the Lumeva range of medical grade skin care products in many of our treatments. Lumeva products are also available for retail sale to assist you in caring for your pre- and post-treatment skin.<br>Book in for a free skin consult if you have used Lumeva products before, or if you are a new client wanting to try one of our starter packs.</p>
    <p>For more information, visit www.lumevaskin.com</p>
    <p>We also stock the popular 'Sole Drift' brand of therapeutic arch support footwear in several different colours - speak to our podiatrists to have a pair professionally fitted.</p>
  </div>
</section>

<section class="contact" id="contact">
  <div class="photo contact-photo" role="img" aria-label="Woman smelling an orchid"></div>
  <h2 class="section-title">Contact Us</h2>
  <form class="contact-form">
    <div class="field">Your Name</div>
    <div class="field">Email</div>
    <div class="field message">Message</div>
    <div class="send">Send</div>
  </form>
  <div class="contact-info">
    <h4>Location:</h4>
    <p>14 Alder Lane, Brightmoor,<br>AU</p>
    <h4>Make an appointment:</h4>
    <p>+61 3 9000 0000</p>
    <h4 style="margin-top:18px">Opening hours:</h4>
    <p style="margin-top:14px">Mon - Fri 9:00 am - 7:00 pm<br>Sat 9:00 am - 5:00 pm Sun -<br>Closed</p>
  </div>
</section>

<section class="map" role="img" aria-label="Street map showing the clinic location"></section>

<footer class="footer">
  <div class="social"><span></span><span></span><span></span><span></span></div>
  <p class="copyright">Copyright © 2007-2014 Fernhollow Glow Clinic. All rights reserved.</p>
</footer>

</body>
</html>
```